Website for an interior designer

We need a new website for Clara Beth Holloway whose new business name is Clara Beth Holloway Interiors. She is a residential interior designer with a mix of modern and contemporary tastes. We are in the process of overhauling her website which is +15 years old and not an accurate reflection of her tastes. The uploaded photos are from some of the houses she has done as well as her logo(s). We would need a section for "About Us" that would have a paragraph of text and bullets showing services and a gallery for photos (~12 total, more to come). A contract page would be optional. The client likes the feel/look of this website: https://www.pondrickstudio.example/ but doesn't want to copy it exactly.

Target Market(s)

Upscale home owners

Industry/Entity Type

Interior Design

Coding

Coded - Design and coding required

Number of Pages Required

4 page

Colors

Designer to choose only greyscale colors for use in the design.

Requirements
Must have
• Home page, about us page, gallery page, contact us page.

```html
<!DOCTYPE html>
<html lang="en">
<head>
<meta charset="utf-8">
<title>Clara Beth Holloway Interiors — Website Design</title>
<link rel="stylesheet" href="https://fonts.googleapis.com/css2?family=Cormorant+Garamond:wght@300;400;500&family=Lato:wght@300;400;700&display=swap">
<style>
  :root{
    --stage:#2e2e2e;
    --paper:#ffffff;
    --mist:#f2f2f2;
    --haze:#e6e6e6;
    --slate:#6e6f6f;
    --slate-dark:#5d5e5e;
    --ink:#3a3a3a;
    --muted:#8a8a8a;
    --footer:#474848;
    --footer-bar:#3b3c3c;
    --footer-text:#c9c9c9;
    --photo-light:#d9dcde;
    --photo-mid:#aeb3b6;
    --photo-warm:#b79a80;
  }
  *{box-sizing:border-box;margin:0;padding:0}
  html,body{width:1200px;height:2784px;overflow:hidden;background:var(--paper)}
  body{position:relative;font-family:'Lato',sans-serif;color:var(--ink)}

  .stage{position:absolute;left:0;top:0;width:1200px;height:2160px;background:var(--stage)}
  .page{position:absolute;left:344px;top:48px;width:512px;height:1992px;background:var(--paper);
        box-shadow:0 30px 40px rgba(0,0,0,.45)}
  .page section,.page header,.page footer{position:absolute;left:0;width:512px}

  .serif{font-family:'Cormorant Garamond',serif;font-weight:400;letter-spacing:.04em}
  .body-copy{font-size:5.5px;line-height:8px;color:var(--muted)}
  .btn{display:inline-block;background:var(--slate-dark);color:#fff;font-size:5px;letter-spacing:.1em;
       text-transform:uppercase;padding:5px 10px}
  .photo{position:absolute}

  /* Wordmark: one font, one weight, one colour */
  .wordmark{font-family:'Lato',sans-serif;font-weight:300;color:var(--slate);
            text-transform:uppercase;letter-spacing:.16em}

  /* Header */
  .site-header{top:0;height:220px;background:linear-gradient(180deg,var(--mist),var(--paper))}
  .brand{position:absolute;top:52px;left:0;width:512px;text-align:center;font-size:9px}
  .nav{position:absolute;top:140px;left:0;width:512px;display:flex;justify-content:center;gap:22px;
       font-size:5px;letter-spacing:.12em;text-transform:uppercase;color:var(--muted)}
  .nav .active{color:var(--ink);border-bottom:1px solid var(--ink);padding-bottom:2px}

  /* Hero */
  .hero{top:220px;height:340px;background:linear-gradient(180deg,var(--paper),var(--mist))}
  .hero-backdrop{position:absolute;left:24px;top:28px;width:220px;height:300px;background:var(--slate)}
  .hero-photo{left:48px;top:28px;width:192px;height:268px;background:linear-gradient(135deg,#eef0f1,var(--photo-light) 55%,var(--photo-mid))}
  .hero-copy{position:absolute;left:308px;top:66px;width:170px}
  .hero-title{font-size:22px;line-height:22px;color:var(--slate);text-transform:uppercase}
  .hero-copy .body-copy{margin:14px 0 16px}

  /* About */
  .about{top:560px;height:360px;background:var(--paper)}
  .about-copy{position:absolute;left:54px;top:70px;width:190px}
  .about-title{font-size:20px;color:var(--slate);text-transform:uppercase;border-bottom:1px solid var(--haze);padding-bottom:6px}
  .about-copy .body-copy{margin:10px 0 20px}
  .about-block{position:absolute;left:376px;top:0;width:136px;height:340px;background:var(--slate)}
  .about-photo-a{left:296px;top:20px;width:120px;height:128px;background:linear-gradient(160deg,var(--photo-warm),#7a6552)}
  .about-photo-b{left:296px;top:160px;width:100px;height:140px;background:linear-gradient(160deg,#e4e7e6,var(--photo-mid))}

  /* Services */
  .services{top:920px;height:400px;background:linear-gradient(180deg,var(--mist),var(--paper))}
  .section-head{position:absolute;top:38px;left:0;width:512px;text-align:center}
  .section-title{font-size:20px;color:var(--slate);text-transform:uppercase}
  .section-head .body-copy{width:150px;margin:6px auto 0}
  .dots{display:flex;justify-content:center;gap:3px;margin-top:8px}
  .dots span{width:3px;height:3px;border-radius:50%;background:var(--slate)}
  .service-cards{position:absolute;top:140px;left:36px;display:flex;gap:12px}
  .service-card{position:relative;width:144px;height:220px;background:var(--haze)}
  .service-card.feature{background:var(--slate)}
  .service-card .photo{left:8px;top:8px;width:128px;height:170px}
  .service-card .btn{position:absolute;left:50%;bottom:12px;transform:translateX(-50%);padding:4px 9px}
  .service-card.feature .btn{background:var(--footer-bar)}

  /* Gallery */
  .gallery{top:1320px;height:460px;background:var(--paper)}
  .gallery .section-head{top:52px}
  .gallery-grid{position:absolute;top:168px;left:44px;width:424px;height:240px;display:grid;
                grid-template-columns:1.25fr 1fr 1fr 1fr;grid-template-rows:1fr 1fr;gap:4px}
  .tile{position:relative}
  .tile.tall{grid-row:span 2}
  .tile-label{position:absolute;left:0;right:0;top:45%;text-align:center;color:#fff;font-size:6px;letter-spacing:.12em;text-transform:uppercase}

  /* Footer */
  .site-footer{top:1800px;height:192px;background:var(--footer);color:var(--footer-text)}
  .footer-brand{position:absolute;left:50px;top:30px;width:120px}
  .footer-brand .wordmark{font-size:6px;color:#e2e2e2;letter-spacing:.12em}
  .footer-brand .body-copy{color:var(--footer-text);margin:8px 0 10px}
  .social{display:flex;gap:6px}
  .social span{width:8px;height:8px;border-radius:50%;border:1px solid var(--footer-text)}
  .footer-col{position:absolute;top:34px;font-size:5px;line-height:9px}
  .footer-col h4{font-family:'Cormorant Garamond',serif;font-weight:500;font-size:8px;color:#e2e2e2;margin-bottom:6px;letter-spacing:.04em}
  .footer-col.links{left:244px}
  .footer-col.offer{left:330px}
  .footer-col.contact{left:412px}
  .footer-bar{position:absolute;left:0;bottom:0;width:512px;height:20px;background:var(--footer-bar);
              font-size:4.5px;color:var(--muted);text-align:center;line-height:20px;letter-spacing:.05em}

  /* Brand sign-off */
  .signoff{position:absolute;left:0;top:2440px;width:1200px;text-align:center}
  .signoff .wordmark{font-size:26px;color:var(--ink);letter-spacing:.2em}
</style>
</head>
<body>
  <div class="stage">
    <div class="page">

      <header class="site-header">
        <div class="brand wordmark">Clara Beth Holloway Interiors</div>
        <nav class="nav">
          <span class="active">Home</span><span>About Us</span><span>Services</span><span>Gallery</span><span>Contact Us</span>
        </nav>
      </header>

      <section class="hero">
        <div class="hero-backdrop"></div>
        <div class="photo hero-photo" role="img" aria-label="Bright white living room with tall windows"></div>
        <div class="hero-copy">
          <h1 class="hero-title serif">State<br>of the Art</h1>
          <p class="body-copy">Considered rooms for modern living, shaped with calm materials, quiet light and lasting detail.</p>
          <span class="btn">Learn More</span>
        </div>
      </section>

      <section class="about">
        <div class="about-copy">
          <h2 class="about-title serif">About Us</h2>
          <p class="body-copy">We design residential interiors that balance modern lines with warm contemporary comfort. Every project begins with listening, then grows through careful planning, honest materials and a calm palette. From a single room to a full home renovation, we guide each step so the finished space feels personal, refined and easy to live in every day.</p>
          <span class="btn">Read More</span>
        </div>
        <div class="about-block"></div>
        <div class="photo about-photo-a" role="img" aria-label="Wooden staircase in a modern home"></div>
        <div class="photo about-photo-b" role="img" aria-label="Light hallway with glass railing"></div>
      </section>

      <section class="services">
        <div class="section-head">
          <h2 class="section-title serif">Services</h2>
          <p class="body-copy">Thoughtful design services for every stage of your home project.</p>
          <div class="dots"><span></span><span></span><span></span></div>
        </div>
        <div class="service-cards">
          <div class="service-card">
            <div class="photo" role="img" aria-label="White modern kitchen" style="background:linear-gradient(150deg,#eef0f0,var(--photo-light))"></div>
            <span class="btn">Details</span>
          </div>
          <div class="service-card feature">
            <div class="photo" role="img" aria-label="Dark dining room interior" style="background:linear-gradient(150deg,#7b7e80,#55585a)"></div>
            <span class="btn">Details</span>
          </div>
          <div class="service-card">
            <div class="photo" role="img" aria-label="Living room with large windows" style="background:linear-gradient(150deg,#d6dadc,var(--photo-mid))"></div>
            <span class="btn">Details</span>
          </div>
        </div>
      </section>

      <section class="gallery">
        <div class="section-head">
          <h2 class="section-title serif">Gallery</h2>
          <p class="body-copy">A selection of finished homes, from open living rooms to quiet bedrooms.</p>
        </div>
        <div class="gallery-grid">
          <div class="tile tall" role="img" aria-label="Sofa corner with a lamp" style="background:linear-gradient(160deg,#d8d4cf,#9fa3a6)"></div>
          <div class="tile" role="img" aria-label="Living room detail" style="background:linear-gradient(160deg,#7c7f81,#5d6163)"><span class="tile-label">Living Room</span></div>
          <div class="tile" role="img" aria-label="Kitchen island" style="background:linear-gradient(160deg,#b59a7f,#8a735e)"></div>
          <div class="tile" role="img" aria-label="Open plan interior" style="background:linear-gradient(160deg,#cfd3d5,#9ea3a6)"></div>
          <div class="tile" role="img" aria-label="Bedroom with soft light" style="background:linear-gradient(160deg,#e5e6e6,#b8bcbe)"></div>
          <div class="tile" role="img" aria-label="Dining area" style="background:linear-gradient(160deg,#a9adaf,#6f7375)"></div>
          <div class="tile" role="img" aria-label="Kitchen in grey tones" style="background:linear-gradient(160deg,#6e7173,#4f5254)"><span class="tile-label">Kitchen</span></div>
        </div>
      </section>

      <footer class="site-footer">
        <div class="footer-brand">
          <div class="wordmark">Clara Beth Holloway</div>
          <p class="body-copy">Residential interiors for modern and contemporary homes.</p>
          <div class="social"><span></span><span></span><span></span><span></span></div>
        </div>
        <div class="footer-col links">
          <h4>Helpful Links</h4>
          <div>Home</div><div>About</div><div>Services</div><div>Gallery</div>
        </div>
        <div class="footer-col offer">
          <h4>Services</h4>
          <div>Space Planning</div><div>Renovation</div><div>Styling</div><div>Furnishing</div>
        </div>
        <div class="footer-col contact">
          <h4>Contact Us</h4>
          <div>(555) 014-2290</div><div>hello@pondrickstudio.example</div>
        </div>
        <div class="footer-bar">© 2024 Clara Beth Holloway Interiors. All rights reserved.</div>
      </footer>

    </div>
  </div>

  <div class="signoff">
    <div class="wordmark">Clara Beth Holloway Interiors</div>
  </div>
</body>
</html>
```